Business card design needed for Renewable utilities company based in New Zealand.

We supply and install solar panels and all components along with it for a fully customisable PV system that helps customer save money on their energy bills right away and also save the planet!

I have attached logo & website design files to give you a better insight.

Industry/Entity Type

Business

```html
<!DOCTYPE html>
<html lang="en">
<head>
<meta charset="utf-8">
<title>Bright Field Energy – Business Card</title>
<link rel="stylesheet" href="https://fonts.googleapis.com/css2?family=Roboto:wght@300;400;500;700&display=swap">
<style>
  :root {
    --backdrop: #e3e3e5;
    --card-white: #ffffff;
    --sky: #2bb0e3;
    --sky-light: #5cc5ec;
    --mist: #eceef3;
    --mark: #3a6fd8;
    --navy: #2b3a67;
    --ink: #3b4150;
    --text-white: #ffffff;
  }
  * { margin: 0; padding: 0; box-sizing: border-box; }
  html, body {
    width: 1200px; height: 479px; overflow: hidden;
    background: var(--backdrop);
    font-family: "Roboto", Arial, sans-serif;
  }
  .canvas { position: relative; width: 1200px; height: 479px; }
  .card {
    position: absolute; top: 85px;
    width: 540px; height: 309px;
    background: var(--card-white);
    overflow: hidden;
    box-shadow: 0 6px 18px rgba(0,0,0,0.12);
  }
  .card-back { left: 40px; }
  .card-front { left: 620px; }
  .card-art { position: absolute; inset: 0; width: 100%; height: 100%; }

  .brand { position: absolute; display: flex; flex-direction: column; align-items: center; }
  .brand-dot { width: 58px; height: 58px; border-radius: 50%; background: var(--mark); }
  .brand-name {
    margin-top: 12px;
    font-weight: 300; font-size: 24px; letter-spacing: 0.5px;
    color: var(--sky); white-space: nowrap;
  }
  .card-back .brand { left: 235px; top: 40px; }

  .services { position: absolute; left: 160px; top: 212px; list-style: none; }
  .services li {
    position: relative; padding-left: 14px;
    font-size: 11px; line-height: 19px; color: var(--ink);
  }
  .services li::before {
    content: ""; position: absolute; left: 0; top: 7px;
    width: 5px; height: 5px; border-radius: 50%; background: var(--sky);
  }

  .holder { position: absolute; left: 28px; top: 34px; color: var(--text-white); }
  .holder-name { font-size: 25px; font-weight: 400; }
  .holder-role { margin-top: 8px; font-size: 15px; font-weight: 400; }

  .contacts { position: absolute; left: 28px; top: 138px; list-style: none; }
  .contacts li {
    display: flex; align-items: center; gap: 10px;
    height: 24px; font-size: 13px; color: var(--text-white);
  }
  .contacts svg { width: 17px; height: 17px; flex: none; }

  .card-front .brand { right: 26px; top: 158px; align-items: flex-end; }
  .card-front .brand-dot { margin-right: 62px; }
  .address {
    position: absolute; right: 26px; top: 276px;
    font-size: 11px; font-weight: 700; color: var(--navy);
  }
</style>
</head>
<body>
<main class="canvas">

  <section class="card card-back" aria-label="Card back">
    <svg class="card-art" viewBox="0 0 540 309" aria-hidden="true">
      <circle cx="20" cy="120" r="200" fill="var(--mist)"/>
      <circle cx="-10" cy="95" r="150" fill="var(--sky)"/>
      <circle cx="40" cy="60" r="70" fill="var(--sky-light)" opacity="0.4"/>
    </svg>
    <div class="brand">
      <span class="brand-dot"></span>
      <span class="brand-name">Bright Field Energy</span>
    </div>
    <ul class="services">
      <li>Solar Panels</li>
      <li>Vertical Axis Wind Turbines</li>
      <li>Atmospheric Water Generators</li>
    </ul>
  </section>

  <section class="card card-front" aria-label="Card front">
    <svg class="card-art" viewBox="0 0 540 309" aria-hidden="true">
      <circle cx="470" cy="250" r="170" fill="var(--mist)"/>
      <path d="M0 0 H450 C420 120 340 220 150 309 H0 Z" fill="var(--sky)"/>
      <circle cx="190" cy="260" r="100" fill="var(--sky-light)" opacity="0.35"/>
    </svg>
    <div class="holder">
      <p class="holder-name">Sam Carter</p>
      <p class="holder-role">Managing Director</p>
    </div>
    <ul class="contacts">
      <li>
        <svg viewBox="0 0 20 20"><rect x="2" y="4" width="16" height="12" fill="none" stroke="#fff" stroke-width="1.5"/><path d="M2 4 L10 11 L18 4" fill="none" stroke="#fff" stroke-width="1.5"/></svg>
        sam.carter@brightfieldenergy.com
      </li>
      <li>
        <svg viewBox="0 0 20 20"><circle cx="10" cy="10" r="8" fill="none" stroke="#fff" stroke-width="1.5"/><ellipse cx="10" cy="10" rx="3.5" ry="8" fill="none" stroke="#fff" stroke-width="1.2"/><path d="M2 10 H18" stroke="#fff" stroke-width="1.2"/></svg>
        www.brightfieldenergy.com
      </li>
      <li>
        <svg viewBox="0 0 20 20"><path d="M3 8 Q10 2 17 8 L15 10 L12 8 L8 8 L5 10 Z" fill="#fff"/><rect x="5" y="11" width="10" height="6" rx="1" fill="#fff"/></svg>
        07 40011238
      </li>
      <li>
        <svg viewBox="0 0 20 20"><rect x="6" y="2" width="8" height="6" fill="none" stroke="#fff" stroke-width="1.5"/><rect x="2" y="8" width="16" height="9" rx="1.5" fill="#fff"/></svg>
        07 40011239
      </li>
    </ul>
    <div class="brand">
      <span class="brand-dot"></span>
      <span class="brand-name">Bright Field Energy</span>
    </div>
    <p class="address">Level 2 48 Harbour Road, Westport 7825</p>
  </section>

</main>
</body>
</html>
```